Harbor Vantage needs new design business card

We are video surveillance and analytics software development company.
I am looking for a professional business card.
Our website is www.harborvantage-example.com.au
Please have a loo and get the feel for who we are and what we do.
I do not know what else to give you apart from good luck and I hope your design gets selected.
Thank you very much for participating
Industry/Entity Type
Business
Contact Information for Business Card
Address
27/14 Pemberly Street Millbrook NSW 2199
Telephone 1300 582 741
Mobile 0450 713 258
email: marcus@harborvantage-example.com.au
name
Marcus Felder
Position
Managing Director
Font styles to use
Other font styles liked:
- Arial
Look and feel

```html
<!DOCTYPE html>
<html lang="en">
<head>
<meta charset="utf-8">
<title>Harbor Vantage – Business Card</title>
<link href="https://fonts.googleapis.com/css2?family=Open+Sans:wght@400;600;700&display=swap" rel="stylesheet">
<style>
  :root {
    --backdrop: #2a2b2e;
    --card-white: #f7f8f9;
    --brand-blue: #1a5fa3;
    --brand-navy: #163e73;
    --accent-orange: #f39c33;
    --panel-grey: #a6a8ab;
    --text-blue: #1f5a9c;
  }
  * { box-sizing: border-box; margin: 0; padding: 0; }
  html, body {
    width: 1200px; height: 900px; overflow: hidden;
    background: var(--backdrop);
    font-family: "Open Sans", Arial, sans-serif;
  }
  .canvas {
    position: relative; width: 1200px; height: 900px;
  }
  .card {
    position: absolute; left: 280px;
    width: 640px; height: 366px;
    background: var(--card-white);
    overflow: hidden;
    box-shadow: 0 10px 30px rgba(0,0,0,.35);
  }
  .card--front { top: 60px; }
  .card--back { top: 474px; }
  .stripe {
    position: absolute; left: 0; width: 100%; height: 16px;
    background: var(--brand-blue);
  }
  .stripe--top { top: 0; }
  .stripe--bottom { bottom: 0; }

  .wordmark {
    position: absolute;
    display: flex; align-items: center; gap: 14px;
    font-weight: 700; color: var(--brand-navy);
    letter-spacing: .5px; white-space: nowrap;
  }
  .wordmark__mark {
    background: var(--brand-navy);
  }
  .card--front .wordmark {
    left: 50%; top: 50%; transform: translate(-50%, -50%);
    font-size: 46px;
  }
  .card--front .wordmark__mark { width: 34px; height: 34px; }
  .card--back .wordmark {
    left: 40px; top: 118px; font-size: 24px; gap: 10px;
  }
  .card--back .wordmark__mark { width: 20px; height: 20px; }

  .contact {
    position: absolute; left: 332px; top: 66px;
    color: var(--text-blue);
  }
  .contact__name { font-size: 22px; font-weight: 700; line-height: 1.15; }
  .contact__role { font-size: 14px; color: var(--accent-orange); margin-bottom: 10px; }
  .contact__list { list-style: none; font-size: 13.5px; line-height: 1.55; }
  .contact__item { display: flex; align-items: center; gap: 10px; }
  .contact__icon { width: 13px; height: 13px; flex: none; }
  .contact__icon * { fill: none; stroke: var(--accent-orange); stroke-width: 1.6; }

  .panel-grey {
    position: absolute; right: 0; top: 208px;
    width: 150px; height: 70px;
    background: var(--panel-grey);
  }
  .address-band {
    position: absolute; left: 0; bottom: 16px;
    width: 100%; height: 72px;
    background: var(--accent-orange);
    display: flex; align-items: center;
    padding-left: 30px;
    color: #fff; font-weight: 700; font-size: 19px;
  }
</style>
</head>
<body>
<main class="canvas">

  <section class="card card--front" aria-label="Business card front">
    <div class="stripe stripe--top"></div>
    <div class="wordmark"><span class="wordmark__mark"></span>Harbor Vantage</div>
    <div class="stripe stripe--bottom"></div>
  </section>

  <section class="card card--back" aria-label="Business card back">
    <div class="stripe stripe--top"></div>
    <div class="wordmark"><span class="wordmark__mark"></span>Harbor Vantage</div>

    <div class="contact">
      <p class="contact__name">Marcus Felder</p>
      <p class="contact__role">Managing Director</p>
      <ul class="contact__list">
        <li class="contact__item">
          <svg class="contact__icon" viewBox="0 0 14 14"><path d="M3 1.5l2 2.5-1.3 1.3a8 8 0 0 0 4.5 4.5L9.5 8.5l2.5 2-1.3 2C6 12.5 1.5 8 1.5 3.3z"/></svg>
          1300 582 741
        </li>
        <li class="contact__item">
          <svg class="contact__icon" viewBox="0 0 14 14"><rect x="3.5" y="1" width="7" height="12" rx="1.2"/><path d="M6 11h2"/></svg>
          0450 713 258
        </li>
        <li class="contact__item">
          <svg class="contact__icon" viewBox="0 0 14 14"><circle cx="7" cy="7" r="5.7"/><path d="M1.3 7h11.4M7 1.3c-3 3-3 8.4 0 11.4M7 1.3c3 3 3 8.4 0 11.4"/></svg>
          www.harborvantage-example.com.au
        </li>
        <li class="contact__item">
          <svg class="contact__icon" viewBox="0 0 14 14"><rect x="1" y="3" width="12" height="8.5" rx=".8"/><path d="M1 3.5l6 4.5 6-4.5"/></svg>
          marcus@harborvantage-example.com.au
        </li>
      </ul>
    </div>

    <div class="panel-grey"></div>
    <div class="address-band">27/14 Pemberly Street Millbrook NSW 2199</div>
    <div class="stripe stripe--bottom"></div>
  </section>

</main>
</body>
</html>
```